Professional Home Buyer business card needed

I need a pretty straight forward business card designed. We help people that NEED to sell their homes solve problems. We perform all types of Real Estate transactions including flip, wholesale, investment, rental property and multi family. The card will mainly be used to give to prospective Sellers but will also be given to Real Estate Investors as well. It should professional and very easy to read, most clients are older people.

Target Market(s)

Distressed home sellers as well as Real Estate investors

Industry/Entity Type

Real Estate

Contact Information for Business Card

should be a professional layout

Colors
ec1f27
ffffff
000000

Requirements
Must have
• Large logo on back and smaller one on front. should utilize Red, white, and black.
• I am thinking of using a soft touch coating on the card so keep that in mind.
• Contact info should be very easy to read, think older clients.
Nice to have
• I would like to see a design with rounded corners on the card
Should not have
• pictures of homes or other home graphics.

```html
<!DOCTYPE html>
<html lang="en">
<head>
<meta charset="utf-8">
<title>Keystone Home Buyers – Business Card</title>
<link href="https://fonts.googleapis.com/css2?family=Open+Sans:wght@400;600;700&display=swap" rel="stylesheet">
<style>
  :root {
    --brand-red: #ec1f27;
    --brand-white: #ffffff;
    --brand-black: #000000;
    --card-black: #161616;
    --text-light: #d4d4d4;
    --text-muted: #bdbdbd;
    --stage: #e9e6e1;
  }
  * { box-sizing: border-box; margin: 0; padding: 0; }
  html, body {
    width: 1200px; height: 900px; overflow: hidden;
    background: var(--stage);
    font-family: "Open Sans", Arial, sans-serif;
  }
  .canvas {
    position: relative; width: 1200px; height: 900px;
    display: flex; flex-direction: column; align-items: center; justify-content: center; gap: 50px;
  }
  .card {
    position: relative; width: 630px; height: 360px;
    background: radial-gradient(ellipse at 50% 40%, #1e1e1e 0%, var(--card-black) 70%, #0f0f0f 100%);
    border-radius: 22px;
    box-shadow: 0 10px 28px rgba(0,0,0,.25);
    color: var(--text-light);
  }
  .wordmark {
    display: flex; align-items: center; gap: 12px;
  }
  .wordmark-square {
    width: 18px; height: 18px; background: var(--brand-red); flex: none;
  }
  .wordmark-name {
    color: var(--text-light); font-weight: 700; letter-spacing: 3px; text-transform: uppercase; white-space: nowrap;
  }
  /* Back */
  .card-back { display: flex; align-items: center; justify-content: center; }
  .card-back .wordmark-name { font-size: 34px; }
  .card-back .wordmark-square { width: 24px; height: 24px; }
  /* Front */
  .card-front .wordmark { position: absolute; top: 62px; right: 44px; }
  .card-front .wordmark-name { font-size: 20px; letter-spacing: 2px; }
  .holder { position: absolute; left: 40px; top: 112px; }
  .holder-name { color: var(--brand-red); font-size: 24px; font-weight: 700; line-height: 1.2; }
  .holder-title { color: var(--text-light); font-size: 16px; margin-top: 2px; }
  .divider { position: absolute; left: 40px; right: 44px; top: 186px; height: 1.5px; background: var(--brand-red); }
  .contact-list { position: absolute; left: 40px; top: 210px; list-style: none; }
  .contact-item { display: flex; align-items: center; gap: 14px; font-size: 17px; line-height: 1.55; }
  .contact-item svg { width: 16px; height: 16px; fill: var(--brand-red); flex: none; }
  .address { position: absolute; right: 44px; bottom: 40px; text-align: right; font-size: 17px; line-height: 1.55; color: var(--text-muted); }
</style>
</head>
<body>
<main class="canvas">
  <section class="card card-back" aria-label="Card back">
    <div class="wordmark">
      <span class="wordmark-square"></span>
      <span class="wordmark-name">Keystone Home Buyers</span>
    </div>
  </section>

  <section class="card card-front" aria-label="Card front">
    <div class="wordmark">
      <span class="wordmark-square"></span>
      <span class="wordmark-name">Keystone Home Buyers</span>
    </div>
    <div class="holder">
      <p class="holder-name">Daniel Mercer</p>
      <p class="holder-title">President</p>
    </div>
    <div class="divider"></div>
    <ul class="contact-list">
      <li class="contact-item">
        <svg viewBox="0 0 24 24" aria-hidden="true"><path d="M6.6 10.8a15.1 15.1 0 0 0 6.6 6.6l2.2-2.2a1 1 0 0 1 1-.25 11.4 11.4 0 0 0 3.6.57 1 1 0 0 1 1 1V20a1 1 0 0 1-1 1A17 17 0 0 1 3 4a1 1 0 0 1 1-1h3.5a1 1 0 0 1 1 1c0 1.25.2 2.46.57 3.6a1 1 0 0 1-.25 1z"/></svg>
        <span>316 - 555 - 0148</span>
      </li>
      <li class="contact-item">
        <svg viewBox="0 0 24 24" aria-hidden="true"><path d="M2 5h20v14H2z" opacity="0"/><path d="M2 6l10 7 10-7v12H2z"/><path d="M2 5h20l-10 7z"/></svg>
        <span>daniel@prairiehomesforcash.com</span>
      </li>
      <li class="contact-item">
        <svg viewBox="0 0 24 24" aria-hidden="true"><path d="M12 2a10 10 0 1 0 0 20 10 10 0 0 0 0-20zm-1 17.9A8 8 0 0 1 4.1 11H7v1a2 2 0 0 0 2 2v2a2 2 0 0 0 2 2zm6.9-2.5A2 2 0 0 0 16 16h-1v-3a1 1 0 0 0-1-1H8v-2h2a1 1 0 0 0 1-1V7h2a2 2 0 0 0 2-2v-.4a8 8 0 0 1 2.9 12.8z"/></svg>
        <span>www.prairiehomesforcash.com</span>
      </li>
    </ul>
    <address class="address" style="font-style:normal">
      P.O. Box 82<br>Elmridge, KS 67010
    </address>
  </section>
</main>
</body>
</html>
```